Need a FLAT UI design for mobile campus Marketplace APP

We need to improve our current UI/UX design for a mobile application called Tradlo. It is designed for students to buy and sell their goods, such as books and furnitures, on their own campus to save living expenses. Our initial design does not look very flat and clear enough. We would like to see a flat design improvement for a better purchasing and selling experience using yellow as theme color.

Target Market(s)

college students

Industry/Entity Type

Marketplace

Colors
ffc214
ffcf3e
fee18a
fff3d1

Requirements
Must have
• an improved UI look, flat and simple.
Nice to have
• alternative designs
Should not have
• a new function design for the app on the design

```html
<!DOCTYPE html>
<html lang="en">
<head>
<meta charset="utf-8">
<title>Tradlo – Home</title>
<link rel="stylesheet" href="https://fonts.googleapis.com/css2?family=Open+Sans:wght@400;600;700&family=Roboto+Condensed:ital,wght@0,400;0,700;1,400&display=swap">
<style>
  :root{
    --yellow:#ffc214;
    --yellow-mid:#ffcf3e;
    --yellow-soft:#fee18a;
    --cream:#fff3d1;
    --ink:#111111;
    --white:#ffffff;
    --orange:#ec5a1c;
    --banner-dark:#1d1a2e;
    --banner-blue:#7d8fc4;
  }
  *{margin:0;padding:0;box-sizing:border-box}
  html,body{width:671px;height:1200px;overflow:hidden;background:var(--yellow)}
  .app{position:relative;width:671px;height:1200px;background:var(--yellow);font-family:"Open Sans",sans-serif;color:var(--ink)}

  .status-bar{position:absolute;left:0;top:0;width:100%;height:29px;background:var(--yellow);display:flex;align-items:center;justify-content:space-between;padding:0 10px;font-size:19px;font-family:"Open Sans",sans-serif}
  .status-bar .carrier{display:flex;align-items:center;gap:6px}
  .status-bar .battery{display:flex;align-items:center;gap:6px}

  .search-bar{position:absolute;left:0;top:29px;width:100%;height:95px;background:var(--yellow-soft)}
  .search-bar .search-icon{position:absolute;left:31px;top:33px}
  .search-bar .clear-btn{position:absolute;left:590px;top:56px;transform:translateY(-50%)}

  .banner{position:absolute;left:23px;top:144px;width:623px;height:442px;overflow:hidden;
    background:linear-gradient(180deg,var(--banner-blue) 0%,#a6b6dd 30%,#6a6a9a 65%,var(--banner-dark) 100%)}
  .banner .product-photo{position:absolute;left:50px;top:60px;width:250px;height:330px;border-radius:40%;
    background:radial-gradient(ellipse at center,#9a6a45 0%,#4b4b52 55%,rgba(60,60,70,0) 75%)}
  .banner .brand{position:absolute;left:276px;top:82px;font-family:"Roboto Condensed",sans-serif;font-size:44px;color:var(--white);letter-spacing:1px}
  .banner .product{position:absolute;left:274px;top:128px;font-family:"Roboto Condensed",sans-serif;font-style:italic;font-size:84px;line-height:1;color:var(--orange);letter-spacing:1px}
  .banner .ribbon{position:absolute;left:396px;top:344px;width:227px;height:48px;background:var(--yellow);
    clip-path:polygon(0 0,100% 0,100% 100%,0 100%,12% 50%);font-family:"Roboto Condensed",sans-serif;font-size:27px;
    display:flex;align-items:center;justify-content:flex-end;padding-right:18px;color:var(--ink)}

  .pager{position:absolute;top:600px;left:0;width:100%;display:flex;justify-content:center;gap:26px}
  .pager span{width:16px;height:16px;border-radius:50%;border:2px solid var(--white)}
  .pager span.active{background:var(--white)}

  .categories{position:absolute;left:20px;top:641px;width:630px;display:grid;grid-template-columns:repeat(3,196px);grid-template-rows:repeat(2,198px);column-gap:21px;row-gap:21px}
  .category{background:var(--yellow-soft);position:relative}
  .category .label{position:absolute;left:0;bottom:8px;width:100%;text-align:center;font-weight:700;font-size:22px;letter-spacing:.5px}
  .category .icons{position:absolute;left:32px;top:20px;width:132px;height:132px;display:grid;grid-template-columns:1fr 1fr;gap:12px}
  .category .icons div{background:var(--cream);display:flex;align-items:center;justify-content:center}
  .category .single{position:absolute;left:29px;top:18px;width:138px;height:130px;background:var(--cream);display:flex;align-items:center;justify-content:center}

  .tab-bar{position:absolute;left:0;top:1099px;width:100%;height:101px;background:var(--yellow-soft)}
  .tab{position:absolute;top:12px;display:flex;flex-direction:column;align-items:center;transform:translateX(-50%);font-size:22px;font-weight:600;gap:4px}
  .tab svg{height:44px}
  .tab.chat{left:44px}.tab.trade{left:185px}.tab.post{left:468px}.tab.profile{left:612px}
  .home-btn{position:absolute;left:331px;top:46px;width:90px;height:90px;transform:translate(-50%,-50%);border-radius:50%;
    background:var(--yellow-mid);border:3px solid var(--cream);box-shadow:inset 0 0 0 6px var(--yellow-soft);display:flex;align-items:center;justify-content:center}
</style>
</head>
<body>
<main class="app">
  <header class="status-bar">
    <div class="carrier">
      <svg width="58" height="12" viewBox="0 0 58 12" fill="#111"><circle cx="6" cy="6" r="5"/><circle cx="17" cy="6" r="5"/><circle cx="28" cy="6" r="5"/><circle cx="40" cy="6" r="4.5" fill="none" stroke="#111"/><circle cx="52" cy="6" r="4.5" fill="none" stroke="#111"/></svg>
      <span>mobile</span>
      <svg width="22" height="16" viewBox="0 0 22 16" fill="none" stroke="#111" stroke-width="2.4"><path d="M2 6a13 13 0 0 1 18 0M5 9.5a8 8 0 0 1 12 0"/><circle cx="11" cy="13" r="1.8" fill="#111" stroke="none"/></svg>
    </div>
    <span class="time">4:21 PM</span>
    <div class="battery">
      <svg width="12" height="18" viewBox="0 0 12 18" fill="none" stroke="#111" stroke-width="1.8"><path d="M2 5l8 8-4 4V1l4 4-8 8"/></svg>
      <span>100%</span>
      <svg width="46" height="20" viewBox="0 0 46 20"><rect x="1" y="2" width="40" height="16" rx="3" fill="none" stroke="#111" stroke-width="2"/><rect x="4" y="5" width="34" height="10" fill="#111"/><rect x="42" y="7" width="3" height="6" fill="#111"/></svg>
    </div>
  </header>

  <div class="search-bar">
    <svg class="search-icon" width="32" height="32" viewBox="0 0 32 32" fill="none" stroke="#fff" stroke-width="4"><circle cx="13" cy="13" r="9"/><path d="M20 20l9 9" stroke-linecap="round"/></svg>
    <svg class="clear-btn" width="42" height="42" viewBox="0 0 42 42"><circle cx="21" cy="21" r="21" fill="var(--yellow)"/><path d="M14 14l14 14M28 14L14 28" stroke="#fff" stroke-width="4.5" stroke-linecap="round"/></svg>
  </div>

  <section class="banner" role="img" aria-label="Promotional photo of over-ear headphones on a blurred blue stage background">
    <div class="product-photo"></div>
    <span class="brand">NORVO</span>
    <span class="product">HEADSET</span>
    <span class="ribbon">BRAND NEW</span>
  </section>

  <nav class="pager"><span></span><span class="active"></span><span></span></nav>

  <section class="categories">
    <div class="category">
      <div class="icons">
        <div><svg width="40" height="40" viewBox="0 0 40 40" fill="var(--yellow)"><path d="M20 4L4 12h32z"/><rect x="6" y="14" width="28" height="3"/><rect x="8" y="19" width="4" height="12"/><rect x="18" y="19" width="4" height="12"/><rect x="28" y="19" width="4" height="12"/><rect x="4" y="33" width="32" height="4"/></svg></div>
        <div><svg width="42" height="36" viewBox="0 0 42 36" fill="var(--yellow)"><path d="M21 4L2 13l19 9 19-9z"/><path d="M10 18v8c6 5 16 5 22 0v-8l-11 5z"/><rect x="37" y="13" width="2" height="12"/></svg></div>
        <div><svg width="34" height="40" viewBox="0 0 34 40" fill="var(--yellow)"><path d="M17 14c-8-4-14 2-12 12 2 9 8 12 12 10 4 2 10-1 12-10 2-10-4-16-12-12z"/><path d="M17 14c0-5 3-9 8-10-1 5-4 8-8 10z"/></svg></div>
        <div><svg width="42" height="22" viewBox="0 0 42 22"><rect x="1" y="1" width="40" height="20" rx="3" fill="var(--yellow)"/><circle cx="12" cy="11" r="3" fill="#fff"/><circle cx="21" cy="11" r="3" fill="#fff"/><circle cx="30" cy="11" r="3" fill="#fff"/></svg></div>
      </div>
      <span class="label">CAMPUS LIFE</span>
    </div>
    <div class="category">
      <div class="icons">
        <div><svg width="42" height="38" viewBox="0 0 42 38" fill="var(--yellow)"><path d="M2 3h38v24H2zM6 7v16h30V7z" fill-rule="evenodd"/><rect x="17" y="27" width="8" height="6"/><rect x="11" y="33" width="20" height="3"/></svg></div>
        <div><svg width="24" height="42" viewBox="0 0 24 42" fill="var(--yellow)"><path d="M3 1h18a2 2 0 0 1 2 2v36a2 2 0 0 1-2 2H3a2 2 0 0 1-2-2V3a2 2 0 0 1 2-2zM4 6v28h16V6z" fill-rule="evenodd"/></svg></div>
        <div><svg width="44" height="28" viewBox="0 0 44 28" fill="var(--yellow)"><path d="M10 2h24c6 0 9 10 9 18 0 6-5 8-9 3l-4-4H14l-4 4c-4 5-9 3-9-3 0-8 3-18 9-18z"/><rect x="9" y="8" width="3" height="9" fill="#fff"/><rect x="6" y="11" width="9" height="3" fill="#fff"/><circle cx="32" cy="10" r="2" fill="#fff"/><circle cx="32" cy="16" r="2" fill="#fff"/></svg></div>
        <div><svg width="42" height="22" viewBox="0 0 42 22"><rect x="1" y="1" width="40" height="20" rx="3" fill="var(--yellow)"/><circle cx="12" cy="11" r="3" fill="#fff"/><circle cx="21" cy="11" r="3" fill="#fff"/><circle cx="30" cy="11" r="3" fill="#fff"/></svg></div>
      </div>
      <span class="label">ELECTRONIC</span>
    </div>
    <div class="category">
      <div class="icons"><div></div><div></div><div></div><div></div></div>
      <span class="label">RECENT</span>
    </div>
    <div class="category">
      <div class="single"><svg width="84" height="60" viewBox="0 0 84 60" fill="none" stroke="var(--yellow)" stroke-width="6" stroke-linejoin="round"><path d="M42 10C32 4 16 4 4 8v46c12-4 28-4 38 2 10-6 26-6 38-2V8C68 4 52 4 42 10zM42 10v46"/></svg></div>
      <span class="label">BOOKS</span>
    </div>
    <div class="category">
      <div class="single"><svg width="88" height="48" viewBox="0 0 88 48"><path d="M2 2h84v14a8 8 0 0 0 0 16v14H2V32a8 8 0 0 0 0-16z" fill="var(--yellow)"/><rect x="26" y="16" width="36" height="16" fill="#fff"/></svg></div>
      <span class="label">TICKETS</span>
    </div>
    <div class="category">
      <div class="single"><svg width="76" height="36" viewBox="0 0 76 36"><rect x="1" y="1" width="74" height="34" rx="5" fill="var(--yellow)"/><circle cx="22" cy="18" r="5.5" fill="#fff"/><circle cx="38" cy="18" r="5.5" fill="#fff"/><circle cx="54" cy="18" r="5.5" fill="#fff"/></svg></div>
      <span class="label">OTHERS</span>
    </div>
  </section>

  <footer class="tab-bar">
    <div class="tab chat"><svg viewBox="0 0 52 44" width="52" fill="none" stroke="var(--yellow)" stroke-width="3"><rect x="4" y="4" width="44" height="28" rx="2"/><path d="M14 32l-4 9 12-9"/></svg><span>CHAT</span></div>
    <div class="tab trade"><svg viewBox="0 0 56 44" width="56" fill="none" stroke="var(--yellow)" stroke-width="3"><path d="M14 36a10 10 0 0 1-2-20 14 14 0 0 1 27-3 11 11 0 0 1 4 22z"/><path d="M20 24h16M20 29h16"/></svg><span>TRADE</span></div>
    <div class="home-btn"><svg width="34" height="32" viewBox="0 0 34 32" fill="#fff"><path d="M17 2L1 16h5v14h8v-9h6v9h8V16h5z"/></svg></div>
    <div class="tab post"><svg viewBox="0 0 44 44" width="44" fill="none" stroke="var(--yellow)" stroke-width="3"><rect x="4" y="8" width="30" height="32"/><path d="M18 28l2-6 18-18 4 4-18 18z"/></svg><span>POST</span></div>
    <div class="tab profile"><svg viewBox="0 0 44 44" width="44"><circle cx="22" cy="22" r="20" fill="var(--yellow)"/><circle cx="22" cy="17" r="7" fill="#fff"/><path d="M9 34c3-7 8-9 13-9s10 2 13 9" fill="#fff"/></svg><span>PROFILE</span></div>
  </footer>
</main>
</body>
</html>
```